PL Dunmore Electric Yard Sign

Looking to have a yard sign designed that we can place at projects we are working on. Most likely will be 18" H x 24" W but flexible that we can increase the size if necessary. It should include our logo, our phone # 555-214-7796, website pldunmoreelectric.example and slogan, built on integrity, driven by excellence. Colors should match our brand.

```html
<!DOCTYPE html>
<html lang="en">
<head>
<meta charset="UTF-8">
<title>PL Dunmore Electric – Yard Sign</title>
<link rel="stylesheet" href="https://fonts.googleapis.com/css2?family=Michroma&family=Open+Sans:ital,wght@0,700;1,700&display=swap">
<style>
  :root {
    --navy: #0d3a73;
    --red: #e3182d;
    --white: #ffffff;
    --backdrop: #eceef1;
  }
  * { margin: 0; padding: 0; box-sizing: border-box; }
  html, body {
    width: 1200px;
    height: 916px;
    overflow: hidden;
    background: var(--backdrop);
  }
  .sign {
    position: absolute;
    left: 50px;
    top: 45px;
    width: 1100px;
    height: 826px;
    background: var(--white);
    border: 9px solid var(--navy);
  }
  .brand {
    position: absolute;
    left: 0; right: 0;
    top: 0;
    height: 398px;
    text-align: center;
  }
  .brand-mark {
    position: absolute;
    left: 50%;
    top: 92px;
    width: 92px;
    height: 92px;
    margin-left: -46px;
    border-radius: 50%;
    background: var(--red);
  }
  .brand-name {
    position: absolute;
    left: 0; right: 0;
    top: 216px;
    font-family: "Michroma", sans-serif;
    font-size: 76px;
    line-height: 1;
    color: var(--red);
  }
  .brand-trade {
    position: absolute;
    left: 0; right: 0;
    top: 328px;
    font-family: "Open Sans", sans-serif;
    font-weight: 700;
    font-size: 38px;
    line-height: 1;
    letter-spacing: 0.46em;
    padding-left: 0.46em;
    color: var(--navy);
  }
  .slogan-band {
    position: absolute;
    left: 0; right: 0;
    top: 398px;
    height: 210px;
    background: var(--navy);
  }
  .band-rule {
    position: absolute;
    left: 40px;
    width: 1002px;
    height: 16px;
  }
  .band-rule.top { top: 22px; }
  .band-rule.bottom { bottom: 22px; }
  .slogan {
    position: absolute;
    left: 0; right: 0;
    top: 76px;
    text-align: center;
    font-family: "Open Sans", sans-serif;
    font-style: italic;
    font-weight: 700;
    font-size: 50px;
    line-height: 1.1;
    letter-spacing: -0.02em;
    color: var(--white);
  }
  .contact {
    position: absolute;
    left: 0; right: 0;
    top: 608px;
    bottom: 0;
    text-align: center;
    font-family: "Michroma", sans-serif;
    color: var(--red);
    -webkit-text-stroke: 1.5px var(--navy);
  }
  .contact-phone {
    position: absolute;
    left: 0; right: 0;
    top: 34px;
    font-size: 58px;
    line-height: 1;
    letter-spacing: 0.04em;
  }
  .contact-web {
    position: absolute;
    left: 0; right: 0;
    top: 128px;
    font-size: 35px;
    line-height: 1;
  }
</style>
</head>
<body>
  <main class="sign">
    <header class="brand">
      <span class="brand-mark" aria-hidden="true"></span>
      <h1 class="brand-name">PL DUNMORE</h1>
      <p class="brand-trade">Electrical Contractor</p>
    </header>

    <section class="slogan-band">
      <svg class="band-rule top" viewBox="0 0 1002 16" aria-hidden="true">
        <polygon points="0,0 1002,0 984,8 18,8" fill="#e3182d"/>
        <rect x="18" y="8" width="966" height="6" fill="#ffffff"/>
      </svg>
      <p class="slogan">Built on integrity, driven by excellence</p>
      <svg class="band-rule bottom" viewBox="0 0 1002 16" aria-hidden="true">
        <rect x="18" y="2" width="966" height="6" fill="#ffffff"/>
        <polygon points="18,8 984,8 1002,16 0,16" fill="#e3182d"/>
      </svg>
    </section>

    <footer class="contact">
      <p class="contact-phone">555-214-7796</p>
      <p class="contact-web">PLDUNMOREELECTRIC.EXAMPLE</p>
    </footer>
  </main>
</body>
</html>
```